Brevard médico-conseils - word template

We are dooing lot of médical report from word document. We dont print the text on a stationnary. We are producting the report and save it in pdf. So I need à word template. I want something more than just hard the logo. I would like the look of a stationnary in the word template.

I put an exemple of report. But the final don't have to look that way. Propose something more acurate.
After that I will need a business card.

Industry/Entity Type

Medical

Requirements
Must have
• We have to do a design that integrate are logo and color. You have the file in the project.
• The wrihting beteen the title must be in times new roman.
Nice to have
• We have 2 offices:
• Québec (Building Val-Doré) 512, ave des Tilleuls, local 210, G2K 4P7 T.418 555-7142 T.418 555-7189
• St-Romuald (Building Carrefour Marbel-Les quais) 2350, boul. des Érables, local 305, G7B 2N4. T.418 555-0263 F.418 555-0398
• Mail: info@BrevardMC.com and expertise@BrevardMC.com
• Web: www.BrevardMC.com
• For now you can type www.PTRV.ca to acces the web site.
Should not have
• The same look that the exemple. Because I want to upgrade the look of the company.

```html
<!DOCTYPE html>
<html lang="fr">
<head>
<meta charset="utf-8">
<title>Brevard médico-conseils – Rapport complémentaire du médecin</title>
<link rel="stylesheet" href="https://fonts.googleapis.com/css2?family=Tinos:wght@400;700&display=swap">
<style>
  :root {
    --blue: #1f5fae;
    --blue-deep: #173f7a;
    --navy: #14213d;
    --orange: #f39322;
    --panel: #e6e8ec;
    --paper: #ffffff;
  }
  * { margin: 0; padding: 0; box-sizing: border-box; }
  html, body { width: 851px; height: 1200px; overflow: hidden; background: var(--paper); }
  body { font-family: "Tinos", "Times New Roman", serif; color: var(--navy); position: relative; }

  .services { position: absolute; left: 14px; top: 12px; list-style: none; color: var(--blue); font-weight: 700; font-size: 15px; line-height: 19px; }

  .brand { position: absolute; right: 22px; top: 40px; display: flex; align-items: center; gap: 14px; }
  .brand-mark { width: 40px; height: 40px; background: var(--orange); }
  .brand-name { font-size: 40px; font-weight: 700; color: var(--blue); letter-spacing: 0.5px; }

  .report-title { position: absolute; left: 0; right: 0; top: 152px; text-align: center; font-size: 25px; font-weight: 700; color: var(--blue); }
  .title-rule { position: absolute; left: 200px; right: 22px; top: 186px; height: 2px; background: var(--blue); }

  .panel { position: absolute; left: 28px; right: 22px; background: var(--panel); border-radius: 0 22px 22px 0; }
  .panel-info { top: 204px; height: 192px; }
  .panel-medical { top: 419px; height: 147px; }
  .panel-tab { position: absolute; left: 0; top: 0; bottom: 0; width: 36px; background: var(--blue); border-right: 5px solid #9bbbe3; display: flex; align-items: center; justify-content: center; }
  .panel-tab span { transform: rotate(-90deg); white-space: nowrap; color: #fff; font-weight: 700; font-size: 17px; letter-spacing: 1.5px; }

  .field { position: absolute; font-size: 15px; font-weight: 700; color: var(--navy); white-space: nowrap; }
  .field .colon { position: absolute; left: 212px; }
  .panel .field { left: 114px; }
  .panel .field .colon { left: 212px; }

  .body-field { left: 142px; }
  .body-field .colon { left: 225px; }

  .radiology-note { position: absolute; left: 0; right: 0; top: 746px; text-align: center; font-size: 21px; font-weight: 700; color: var(--blue); }

  .date-field { left: 688px; }

  .footer-rule { position: absolute; left: 14px; right: 14px; top: 1004px; height: 3px; background: var(--orange); }
  .office { position: absolute; top: 1016px; font-size: 12.5px; line-height: 16px; color: var(--navy); }
  .office h3 { font-size: 13.5px; font-weight: 700; }
  .office-quebec { left: 18px; }
  .office-romuald { right: 20px; text-align: right; }
  .contact-line { position: absolute; left: 18px; top: 1118px; font-size: 11.5px; color: var(--navy); }

  .footer-band { position: absolute; left: 0; bottom: 0; width: 851px; height: 58px; }
</style>
</head>
<body>
  <ul class="services">
    <li>Expertise</li>
    <li>Service santé</li>
    <li>Pré-emploi</li>
    <li>Bilan essentiel</li>
    <li>Vaccination</li>
  </ul>

  <div class="brand">
    <div class="brand-mark"></div>
    <div class="brand-name">Brevard médico-conseils</div>
  </div>

  <h1 class="report-title">RAPPORT COMPLÉMENTAIRE DU MÉDECIN</h1>
  <div class="title-rule"></div>

  <section class="panel panel-info">
    <div class="panel-tab"><span>INFORMATION</span></div>
    <div class="field" style="top:14px">NO. DE DOSSIER<span class="colon">:</span></div>
    <div class="field" style="top:39px">EMPLOYEUR<span class="colon">:</span></div>
    <div class="field" style="top:64px">EMPLOYÉ(E)<span class="colon">:</span></div>
    <div class="field" style="top:109px">POSTE<span class="colon">:</span></div>
    <div class="field" style="top:134px">DATE DE L'EXAMEN<span class="colon">:</span></div>
  </section>

  <section class="panel panel-medical">
    <div class="panel-tab"><span>MÉDICAL</span></div>
    <div class="field" style="top:10px">ANTÉCÉDENTS<span class="colon">:</span></div>
  </section>

  <div class="field body-field" style="top:572px">EXAMEN PHYSIQUE<span class="colon">:</span></div>
  <div class="field body-field" style="top:620px">RECOMMANDATIONS<span class="colon">:</span></div>
  <div class="field body-field" style="top:700px">DOSSIER DE CNRT<span class="colon">:</span></div>

  <p class="radiology-note">(Pour la description exacte - voir le rapport de radiologie)</p>

  <div class="field body-field" style="top:798px">RX-LOMBAIRE<span class="colon">:</span></div>
  <div class="field body-field" style="top:836px">MÉDECIN<span class="colon">:</span></div>
  <div class="field body-field" style="top:866px">RÉDACTION<span class="colon">:</span></div>
  <div class="field body-field" style="top:896px">VALIDATION<span class="colon">:</span></div>
  <div class="field date-field" style="top:896px">DATE:</div>

  <div class="footer-rule"></div>

  <address class="office office-quebec" style="font-style:normal">
    <h3>QUÉBEC</h3>
    BUILDING VAL-DORÉ<br>
    512, AVE DES TILLEULS,<br>
    LOCAL 210, G2K 4P7<br>
    T. 418 555-7142 &nbsp;T. 418 555-7189
  </address>

  <address class="office office-romuald" style="font-style:normal">
    <h3>ST-ROMUALD</h3>
    BUILDING CARREFOUR MARBEL-LES QUAIS<br>
    2350, BOUL. DES ÉRABLES,<br>
    LOCAL 305, G7B 2N4<br>
    T. 418 555-0263 &nbsp;F. 418 555-0398
  </address>

  <p class="contact-line">Mail: info@BrevardMC.com AND expertise@BrevardMC.com, Web: www.BrevardMC.com, (www.PTRV.ca to access the web site.)</p>

  <svg class="footer-band" viewBox="0 0 851 58" preserveAspectRatio="none" aria-hidden="true">
    <polygon points="0,58 0,36 500,36 560,14 851,14 851,58" fill="var(--blue)"/>
    <polygon points="0,30 495,30 555,8 851,8 851,12 558,12 498,34 0,34" fill="var(--orange)"/>
  </svg>
</body>
</html>
```